Criação de Papelaria Profissional para Construção & Engenharia
" Nós extraimos o material e o beneficiamos em uma planta de britagem onde resulta no produto final utilizado para os diversos segmentos da construção civil e uso de um produto específico como remineralizador de solo voltado para agricultura "

```html
<!DOCTYPE html>
<html lang="pt-BR">
<head>
<meta charset="UTF-8">
<title>Pedreira Serrana – Assinatura</title>
<link href="https://fonts.googleapis.com/css2?family=Montserrat:wght@500;600;700&family=Open+Sans:wght@400;700&display=swap" rel="stylesheet">
<style>
  :root {
    --navy: #123a7c;
    --gold: #c9a032;
    --grey: #a9abae;
    --white: #ffffff;
    --page: #efefef;
    --ink: #1c2e5c;
  }
  * { margin: 0; padding: 0; box-sizing: border-box; }
  html, body { width: 1200px; height: 1200px; overflow: hidden; }
  body { background: var(--page); position: relative; font-family: "Open Sans", sans-serif; }

  .signature {
    position: absolute; left: 115px; top: 460px;
    width: 970px; height: 260px;
    background: var(--white);
    box-shadow: 0 4px 14px rgba(0,0,0,.12);
    overflow: hidden;
  }
  .signature__shapes { position: absolute; inset: 0; }

  .brand-name {
    position: absolute; left: 72px; top: 120px;
    font-family: "Montserrat", sans-serif; font-weight: 500;
    font-size: 38px; line-height: 44px; letter-spacing: 1px;
    color: var(--white); text-transform: uppercase;
  }

  .person { position: absolute; left: 557px; top: 30px; }
  .person__name {
    font-family: "Montserrat", sans-serif; font-weight: 600;
    font-size: 29px; color: var(--ink); letter-spacing: .5px;
  }
  .person__role {
    font-family: "Montserrat", sans-serif; font-weight: 700;
    font-size: 12px; color: var(--gold); letter-spacing: .5px; margin-top: 1px;
  }

  .contacts { position: absolute; left: 557px; top: 92px; list-style: none; }
  .contacts__item { display: flex; align-items: center; gap: 14px; height: 44px; margin-bottom: 4px; }
  .contacts__icon { width: 20px; height: 20px; flex: none; fill: var(--gold); }
  .contacts__text { font-size: 14px; line-height: 18px; color: var(--ink); }
  .contacts__text b { font-weight: 700; }
</style>
</head>
<body>
  <section class="signature">
    <svg class="signature__shapes" viewBox="0 0 970 260" width="970" height="260">
      <path fill="var(--navy)" d="M0 0 H512 C470 55 452 150 456 260 H0 Z"/>
      <path fill="var(--grey)" d="M512 0 H548 C500 45 474 115 463 205 C462 120 478 50 512 0 Z"/>
      <path fill="var(--gold)" d="M463 260 C455 195 466 140 492 95 C478 150 476 205 494 260 Z"/>
    </svg>

    <div class="brand-name">Pedreira<br>Serrana</div>

    <div class="person">
      <div class="person__name">NOME COMPLETO</div>
      <div class="person__role">CARGO OU FUNÇÃO</div>
    </div>

    <ul class="contacts">
      <li class="contacts__item">
        <svg class="contacts__icon" viewBox="0 0 24 24"><path d="M6.6 10.8a15.2 15.2 0 0 0 6.6 6.6l2.2-2.2c.3-.3.7-.4 1-.2 1.1.4 2.3.6 3.6.6.6 0 1 .4 1 1V20c0 .6-.4 1-1 1A17 17 0 0 1 3 4c0-.6.4-1 1-1h3.5c.6 0 1 .4 1 1 0 1.3.2 2.5.6 3.6.1.3 0 .7-.2 1L6.6 10.8Z"/></svg>
        <span class="contacts__text">00 0000.00000<br>00 0000.00000</span>
      </li>
      <li class="contacts__item">
        <svg class="contacts__icon" viewBox="0 0 24 24"><circle cx="12" cy="12" r="10"/><path d="M2 12h20M12 2c3 3 3 17 0 20M12 2c-3 3-3 17 0 20" stroke="#fff" stroke-width="1.4" fill="none"/></svg>
        <span class="contacts__text"><b>pedreiraserrana</b>.com.br<br><b>contato@pedreiraserrana</b>.com.br</span>
      </li>
      <li class="contacts__item">
        <svg class="contacts__icon" viewBox="0 0 24 24"><path d="M12 2a7 7 0 0 0-7 7c0 5 7 13 7 13s7-8 7-13a7 7 0 0 0-7-7Zm0 9.5A2.5 2.5 0 1 1 12 6.5a2.5 2.5 0 0 1 0 5Z"/></svg>
        <span class="contacts__text">Nome da <b>rua, 000</b> - bairro<br><b>cidade</b> - estado - <b>cep</b> e país</span>
      </li>
    </ul>
  </section>
</body>
</html>
```